Flyer Lieferservice / Gutschein / Visitenkarte
Zielgruppe
Restaurant
Aufgabenstellung
Wir benötigen:
Lieferservice Flyer mit Speisekarte
Gutschein Flyer
Visitenkarten
Farbe: Schwarz & Gold siehe Website
Speisekarte: (siehe Anhang)
Wichtige Inhalte:
Speiskarte
Social Media
Anschrift
Telefonnummer
Website
App Verweis
(bishergie Flyer zur Ansicht im Anhang)

```html
<!DOCTYPE html>
<html lang="de">
<head>
<meta charset="utf-8">
<title>Zur Goldamsel – Lieferservice Flyer</title>
<link href="https://fonts.googleapis.com/css2?family=Great+Vibes&family=Dancing+Script:wght@500&family=Raleway:wght@400;500;600&display=swap" rel="stylesheet">
<style>
  :root{
    --bg:#d9d8d4;
    --menu:#4a463e;
    --black:#111111;
    --gold:#d9a824;
    --gold-text:#d4a52a;
    --white:#ffffff;
    --paper:#efefed;
    --ink:#2a2a2a;
    --muted:#e6e3dc;
  }
  *{box-sizing:border-box;margin:0;padding:0}
  html,body{width:1200px;height:960px;overflow:hidden;background:var(--bg);font-family:"Raleway",sans-serif}
  .flyer{position:absolute;top:100px;width:540px;height:760px;overflow:hidden}

  /* Speisekarte */
  .menu{left:40px;background:var(--menu);color:var(--white);padding:28px 34px 20px 0}
  .section{margin-bottom:12px}
  .section-bar{display:flex;align-items:center;width:230px;height:34px;background:var(--gold);border-radius:0 17px 17px 0;padding-left:34px;margin-bottom:6px}
  .section-title{font-family:"Great Vibes",cursive;font-size:32px;line-height:1;color:var(--white);font-weight:400}
  .items{list-style:none;padding-left:34px}
  .item{display:flex;justify-content:space-between;gap:10px;font-size:9.2px;line-height:12.6px}
  .item b{font-weight:600}
  .item .desc{color:var(--muted)}
  .price{white-space:nowrap;color:var(--muted)}
  .extras{padding-left:34px;font-size:9px;color:var(--gold-text);margin-top:4px;display:flex;gap:28px}
  .note{padding-left:34px;font-size:9px;color:var(--muted);margin-bottom:3px}
  .dressing{padding-left:34px;font-size:9px;color:var(--gold-text);margin-top:6px}

  /* Titelseite */
  .cover{left:620px;background:var(--black);color:var(--white)}
  .frame{position:absolute;left:14px;top:14px;right:14px;height:520px;border:1.5px solid var(--white)}
  .photo{position:absolute;left:150px;top:150px;width:390px;height:350px;
    background:radial-gradient(ellipse at 60% 55%,#7a4a22 0%,#4a2a14 35%,#1d1510 70%,#111 100%)}
  .brand{position:absolute;left:40px;top:50px;display:flex;align-items:center;gap:14px}
  .brand-dot{width:44px;height:44px;border-radius:50%;border:1.5px solid var(--gold)}
  .brand-name{font-size:26px;font-weight:500;color:var(--gold-text);letter-spacing:.5px}
  .web{position:absolute;left:98px;top:92px;font-size:12px;color:var(--white)}
  .order-band{position:absolute;left:0;top:455px;width:270px;height:42px;background:#1b1b1b;display:flex;align-items:center;justify-content:center;font-size:16px;letter-spacing:3px;font-weight:500}
  .phone-pill{position:absolute;left:262px;top:445px;width:262px;height:52px;background:var(--gold);border-radius:26px;display:flex;align-items:center;justify-content:center;font-size:20px;letter-spacing:3px;font-weight:600;color:var(--white)}
  .panel{position:absolute;left:0;top:500px;width:540px;height:260px;background:var(--paper);color:var(--ink);padding:22px 36px}
  .app-title{font-family:"Dancing Script",cursive;font-size:34px;font-weight:500;text-align:center}
  .badges{display:flex;justify-content:center;gap:26px;margin-top:16px}
  .badge{width:124px;height:38px;background:var(--black);border-radius:7px}
  .rule{height:1px;background:#555;margin:20px 30px 14px}
  .info{font-size:10px;line-height:15px;color:var(--ink);text-align:center}
  .info b{color:var(--gold-text);font-weight:600}
</style>
</head>
<body>

<section class="flyer menu" aria-label="Speisekarte">
  <div class="section">
    <div class="section-bar"><h2 class="section-title">Fleisch</h2></div>
    <ul class="items">
      <li class="item"><span><b>Schnitzel „Wiener Art"</b> <span class="desc">mit Beilagen &amp; Soße nach Wahl</span></span><span class="price">klein 7,90 EUR | groß 11,90 EUR</span></li>
      <li class="item"><span><b>Putenschnitzel</b> <span class="desc">mit Beilagen &amp; Soße nach Wahl</span></span><span class="price">klein 9,90 EUR | groß 13,90 EUR</span></li>
      <li class="item"><span><b>Wiener Schnitzel</b> <span class="desc">vom Kalb mit Beilagen &amp; Soße nach Wahl</span></span><span class="price">18,90 EUR</span></li>
      <li class="item"><span><b>Cordon Bleu</b> <span class="desc">mit Beilagen &amp; Soße nach Wahl</span></span><span class="price">14,90 EUR</span></li>
      <li class="item"><span><b>Sonne Cordon Bleu</b> <span class="desc">| Gefüllt mit Tomate-Mozzarella und frischem Basilikum &amp; Beilage/Soße</span></span><span class="price">16,90 EUR</span></li>
      <li class="item"><span><b>Weiden Cordon Bleu</b> <span class="desc">| Gefüllt mit Ziegenfrischkäse, Schinken und Honig &amp; Beilage/Soße</span></span><span class="price">16,90 EUR</span></li>
      <li class="item"><span><b>Mediterranes Cordon Bleu</b> <span class="desc">| gefüllt mit Schafskäse, Oliven und Pepperonis &amp; Beilage/Soße</span></span><span class="price">16,90 EUR</span></li>
      <li class="item"><span><b>Krustenschnitzel</b> <span class="desc">| Schweineschnitzel mit Goudakäse und Jägersoße überbacken &amp; Beilage</span></span><span class="price">13,90 EUR</span></li>
      <li class="item"><span><b>Schnitzel Bolognese</b> <span class="desc">mit Beilage nach Wahl</span></span><span class="price">14,90 EUR</span></li>
      <li class="item"><span><b>Schnitzel Hawaii</b> <span class="desc">mit Beilagen &amp; Soße nach Wahl</span></span><span class="price">14,90 EUR</span></li>
      <li class="item"><span><b>Rinderbraten</b> <span class="desc">mit Beilagen nach Wahl</span></span><span class="price">15,90 EUR</span></li>
      <li class="item"><span><b>Wildragout</b> <span class="desc">mit Beilagen nach Wahl</span></span><span class="price">15,90 EUR</span></li>
      <li class="item"><span><b>Zartes Rindergulasch mit Spätzle</b></span><span class="price">16,90 EUR</span></li>
      <li class="item"><span><b>Puten-Nuggets mit Pommes</b></span><span class="price">klein 5,90 EUR | groß 8,90 EUR</span></li>
      <li class="item"><span><b>Spaghetti Bolognese</b></span><span class="price">klein 7,80 EUR | groß 9,90 EUR</span></li>
    </ul>
    <p class="extras"><span>BEILAGEN Pommes | Kroketten | Spätzle</span><span>SOSSEN Bratensoße | Jägersoße | Pikante Paprikasoße</span></p>
  </div>

  <div class="section">
    <div class="section-bar"><h2 class="section-title">Vegetarisch</h2></div>
    <ul class="items">
      <li class="item"><span><b>Kräuterpfannkuchen gefüllt mit Champignons</b></span><span class="price">10,90 EUR</span></li>
      <li class="item"><span><b>Käsespätzle</b></span><span class="price">klein 7,90 EUR | groß 10,90 EUR</span></li>
      <li class="item"><span><b>Selbstgemachte Serviettenknödel mit Jägersoße</b></span><span class="price">7,90 EUR</span></li>
      <li class="item"><span><b>Gegrillter Schafskäse</b> <span class="desc">| Knoblauch, Zwiebeln, Oliven, Paprika, Tomaten, Peperoni</span></span><span class="price">7,90 EUR</span></li>
    </ul>
  </div>

  <div class="section">
    <div class="section-bar"><h2 class="section-title">Fisch</h2></div>
    <ul class="items">
      <li class="item"><span><b>Kräuterlachs aus dem Ofen mit Kartoffelsalat</b></span><span class="price">17,90 EUR</span></li>
      <li class="item"><span><b>Paniertes Zanderfilet mit Kartoffelsalat</b></span><span class="price">15,90 EUR</span></li>
    </ul>
  </div>

  <div class="section">
    <div class="section-bar"><h2 class="section-title">Salat</h2></div>
    <p class="note">Alle Salate werden serviert mit Krautsalat, Karottensalat, Rotkohlsalat, grüner Salat, Tomate &amp; Gurke</p>
    <ul class="items">
      <li class="item"><span><b>Beilagensalat</b></span><span class="price">4,50 EUR</span></li>
      <li class="item"><span><b>Kartoffelsalat</b></span><span class="price">4,50 EUR</span></li>
      <li class="item"><span><b>Gemischter Salat</b></span><span class="price">7,90 EUR</span></li>
      <li class="item"><span><b>Fitnessalat mit Putenstreifen</b></span><span class="price">11,90 EUR</span></li>
      <li class="item"><span><b>Salat mit Gemüsemaultaschen</b></span><span class="price">11,90 EUR</span></li>
      <li class="item"><span><b>Salat Schafskäse mit Oliven und Pepperonis</b></span><span class="price">10,90 EUR</span></li>
      <li class="item"><span><b>Salat mit Schinken/Käse und Zwiebeln</b></span><span class="price">9,80 EUR</span></li>
    </ul>
    <p class="dressing">Als Dressing stehen wahlweise unser Hausdressing oder Balsamico Honig-Senf Dressing zur Verfügung</p>
  </div>
</section>

<section class="flyer cover" aria-label="Titelseite Lieferservice">
  <div class="photo" role="img" aria-label="Foto: geröstete Ofenkartoffeln mit Kräutern in einer dunklen Pfanne"></div>
  <div class="frame"></div>
  <div class="brand">
    <span class="brand-dot"></span>
    <span class="brand-name">Zur Goldamsel</span>
  </div>
  <p class="web">www.zurgoldamsel.de</p>
  <div class="order-band">BESTELLE UNTER</div>
  <div class="phone-pill">01234 | 5678900</div>
  <div class="panel">
    <h1 class="app-title">Liefershop – jetzt auch als App</h1>
    <div class="badges">
      <span class="badge"></span>
      <span class="badge"></span>
    </div>
    <div class="rule"></div>
    <p class="info"><b>Öffnungszeiten:</b> Mittwoch - Samstag von 17 Uhr bis 21:30 | Sonn- und Feiertag von 11 Uhr bis 21:30 Uhr</p>
    <p class="info"><b>Liefergebiete:</b> Lindenau | Bergfeld | Eichental | Grabenau | Stutzbach | Karlsau | Neuwies bzw. PLZ 12345</p>
  </div>
</section>

</body>
</html>
```